Business Intelligence Dashboard header

We are a top 10 cancer treatment clinic. Our analytics teams (Corporate Finance, Financial Analytics, and Clinical Analytics) are searching for a great graphic to show our business partners the value of our business intelligence products. We are hoping to convey that we are tech-savvy, supportive to our patients and mission of saving lives, valuable, forward-thinking, agile, supportive, and friendly.

This header will be placed at the top of each data visualization ('viz') that we create. We would like a design that is in-line with our company branding, simple, elegant, and striking. We primarily create headers that are between 800 and 1300 pixels across (800 and 1300 being the most common) and between 60 and 80 pixels high (76 being our current header height in px, but we are open to slight deviation.) The type of data visualizations this will sit atop (everything we produce, but just a few examples) will be things like patient safety, clinic utilization, appointment volumes, provider scorecards, and many more. I've included our current header, and a header I saw and liked (although I think it could have been a bit cooler.)

I'm open to ideas, feedback, and your opinion as a designer to come up with something amazing. You can find our website at https://www.brindlemoorhc.org/
Zorpling our business shows our main clinic (with the rounded front) https://www.zorpfind.example/search?q=brindlemoor+oncology+wellness+group&source=lnms&tbm=isch&sa=X&ved=0ahQWErtyu81plMNBvCXzKJd93QwERtyu_AUIDCgD&biw=1995&bih=916

We are open to stock images.

• A place to write in a dashboard title (we will use our own BI-native object to float over the top of this banner)
• We would like a place/icon to differentiate between work products coming out of Clinical Analytics/Financial Analytics/Corporate Finance. We're fine with it being on 2 lines, or simply designing an icon to differentiate. We could use smaller text underneath the dashboard title (see must haves), an icon for each of the 3 teams, or a space in the header to write in the team ourselves. The team names should be of limited significance on the header. The star of the show will be the dashboard title (just leave an area for it) where the team names should be of less significance (off to the side, under the title in smaller font, etc)

```html
<!DOCTYPE html>
<html lang="en">
<head>
<meta charset="utf-8">
<title>Dashboard Header Variants</title>
<link rel="stylesheet" href="https://fonts.googleapis.com/css2?family=Catamaran:wght@400;500;600&display=swap">
<style>
  :root {
    --page-bg: #ffffff;
    --brand-grey: #6d696e;
    --brand-teal: #5bbcb3;
    --brand-teal-deep: #3f9f98;
    --brand-yellow: #f8c92a;
    --text-light: #ffffff;
  }
  * { box-sizing: border-box; margin: 0; padding: 0; }
  html, body {
    width: 1200px;
    height: 326px;
    overflow: hidden;
    background: var(--page-bg);
  }
  .header-set {
    position: relative;
    width: 1200px;
    height: 326px;
    padding: 24px 0 0 27px;
    display: flex;
    flex-direction: column;
    gap: 29px;
  }
  .viz-header {
    position: relative;
    width: 1141px;
    height: 70px;
    display: flex;
    background: var(--brand-teal);
    box-shadow: 0 8px 12px rgba(0, 0, 0, 0.18);
    overflow: hidden;
  }
  .brand-block {
    width: 116px;
    height: 100%;
    background: var(--brand-grey);
    display: flex;
    align-items: center;
    padding-left: 13px;
  }
  .brand-name {
    font-family: "Catamaran", sans-serif;
    font-weight: 600;
    font-size: 14px;
    line-height: 15px;
    color: var(--text-light);
    width: 90px;
  }
  .accent-bar {
    width: 7px;
    height: 100%;
    background: var(--brand-yellow);
  }
  .title-band {
    position: relative;
    flex: 1;
    height: 100%;
  }
  .building-photo {
    position: absolute;
    left: 437px;
    top: 0;
    width: 320px;
    height: 100%;
    background: linear-gradient(90deg,
      rgba(63, 159, 152, 0) 0%,
      rgba(63, 159, 152, 0.75) 20%,
      var(--brand-teal-deep) 50%,
      rgba(63, 159, 152, 0.75) 80%,
      rgba(63, 159, 152, 0) 100%);
  }
  .dashboard-title {
    position: absolute;
    left: 26px;
    top: 50%;
    transform: translateY(-45%);
    font-family: "Catamaran", sans-serif;
    font-weight: 400;
    font-size: 52px;
    line-height: 1;
    color: var(--text-light);
    white-space: nowrap;
  }
  .team-label {
    position: absolute;
    right: 34px;
    top: 50%;
    transform: translateY(-45%);
    font-family: "Catamaran", sans-serif;
    font-weight: 400;
    font-size: 21px;
    line-height: 1;
    color: var(--text-light);
    white-space: nowrap;
  }
  .edge-swoosh {
    position: absolute;
    right: 0;
    top: 0;
    width: 14px;
    height: 100%;
  }
</style>
</head>
<body>
  <main class="header-set">
    <section class="viz-header">
      <div class="brand-block">
        <span class="brand-name">Brindlemoor Health Care</span>
      </div>
      <div class="accent-bar"></div>
      <div class="title-band">
        <div class="building-photo" role="img" aria-label="Teal-tinted photo of the rounded front of the main clinic building"></div>
        <h1 class="dashboard-title">Dashboard Title</h1>
        <p class="team-label">Clinical Analytics</p>
        <svg class="edge-swoosh" viewBox="0 0 14 70" preserveAspectRatio="none" aria-hidden="true">
          <path d="M14 0 L7 0 Q9 40 0 70 L14 70 Z" fill="var(--brand-yellow)"/>
        </svg>
      </div>
    </section>

    <section class="viz-header">
      <div class="brand-block">
        <span class="brand-name">Brindlemoor Health Care</span>
      </div>
      <div class="accent-bar"></div>
      <div class="title-band">
        <div class="building-photo" role="img" aria-label="Teal-tinted photo of the rounded front of the main clinic building"></div>
        <h1 class="dashboard-title">Dashboard Title</h1>
        <p class="team-label">Financial Analytics</p>
        <svg class="edge-swoosh" viewBox="0 0 14 70" preserveAspectRatio="none" aria-hidden="true">
          <path d="M14 0 L7 0 Q9 40 0 70 L14 70 Z" fill="var(--brand-yellow)"/>
        </svg>
      </div>
    </section>

    <section class="viz-header">
      <div class="brand-block">
        <span class="brand-name">Brindlemoor Health Care</span>
      </div>
      <div class="accent-bar"></div>
      <div class="title-band">
        <div class="building-photo" role="img" aria-label="Teal-tinted photo of the rounded front of the main clinic building"></div>
        <h1 class="dashboard-title">Dashboard Title</h1>
        <p class="team-label">Corporate Finance</p>
        <svg class="edge-swoosh" viewBox="0 0 14 70" preserveAspectRatio="none" aria-hidden="true">
          <path d="M14 0 L7 0 Q9 40 0 70 L14 70 Z" fill="var(--brand-yellow)"/>
        </svg>
      </div>
    </section>
  </main>
</body>
</html>
```